Membership card design for video game arena

I need a two sided design for membership cards for my customers. It needs to have instructions on how to book on one side, and a nice catchy design for the other.

Please pull logo and whatever you desire from the website www.vornik-play.com

Industry/Entity Type

Entertainment

Contact Information for Business Card

The front must say Vornik-Play with the address and whatever design you choose. The back must have the details below

Colors

Designer to choose colors to be used in the design.

Requirements
Must have
• Frontside
• Company name address and phone number
• Backside
• Booking Instructions
• www.Vornik-Play.com/book-now
• Click on General Admission and input information
• Use code Gatepass7 to gain access
• See you there!
Nice to have
• A nice design and whatever you find is pertinent
Should not have
• Useless info

```html
<!DOCTYPE html>
<html lang="en">
<head>
<meta charset="utf-8">
<title>Vornik-Play Membership Card</title>
<link rel="stylesheet" href="https://fonts.googleapis.com/css2?family=Open+Sans:wght@400;600;700&display=swap">
<style>
  :root {
    --backdrop-top: #c4d0da;
    --backdrop-bottom: #95a8b7;
    --card-glass-top: #e4ecf2;
    --card-glass-bottom: #c3d1dc;
    --card-edge: rgba(255,255,255,0.8);
    --band-dark: #0b0d11;
    --band-mid: #1c2028;
    --rule-silver: #c9ced4;
    --accent-blue: #3d52c4;
    --arrow-blue: #5a6fe0;
    --text-light: #f3f4f6;
    --text-grey: #b4b8bd;
    --brand-steel: #59636d;
    --photo-light: #a9b6c2;
    --photo-mid: #4c5662;
    --photo-dark: #1f252d;
  }
  * { box-sizing: border-box; margin: 0; padding: 0; }
  html, body { width: 1200px; height: 792px; overflow: hidden; }
  body {
    position: relative;
    font-family: "Open Sans", sans-serif;
    background: linear-gradient(180deg, var(--backdrop-top), var(--backdrop-bottom));
  }
  .card {
    position: absolute;
    top: 232px;
    width: 522px;
    height: 334px;
    border-radius: 18px;
    overflow: hidden;
    border: 1px solid var(--card-edge);
    background: linear-gradient(180deg, var(--card-glass-top), var(--card-glass-bottom));
    box-shadow: 0 6px 18px rgba(40,55,70,0.25);
  }
  .card--front { left: 55px; }
  .card--back { left: 625px; }
  .card__hero {
    position: absolute;
    left: 0; top: 0; width: 100%; height: 196px;
  }
  .hero-photo {
    position: absolute;
    left: 78px; top: 18px; width: 352px; height: 130px;
    border-radius: 10px;
    background:
      radial-gradient(ellipse 38% 70% at 50% 45%, var(--photo-dark) 0%, var(--photo-mid) 55%, transparent 100%),
      linear-gradient(90deg, var(--photo-mid) 0%, var(--photo-light) 22%, var(--photo-light) 78%, var(--photo-mid) 100%);
    border: 1px solid rgba(255,255,255,0.6);
    box-shadow: 0 4px 12px rgba(30,40,50,0.25);
  }
  .card--back .hero-photo {
    opacity: 0.32;
    box-shadow: none;
  }
  .brand {
    position: absolute;
    left: 120px; top: 150px;
    display: flex; align-items: center; gap: 10px;
  }
  .brand__dot {
    width: 36px; height: 36px; border-radius: 50%;
    background: var(--brand-steel);
  }
  .brand__name {
    font-weight: 700; font-size: 32px; letter-spacing: 1px; line-height: 40px;
    color: var(--brand-steel); text-transform: uppercase;
  }
  .card--back .brand { opacity: 0.3; left: 112px; }
  .card__band {
    position: absolute;
    left: 0; top: 196px; width: 100%; height: 138px;
    background: linear-gradient(180deg, var(--band-mid), var(--band-dark));
    border-top: 4px solid var(--rule-silver);
  }
  .contact {
    text-align: center; padding-top: 20px;
  }
  .contact__phone {
    font-size: 20px; color: var(--accent-blue); letter-spacing: 0.5px;
  }
  .contact__address {
    margin-top: 10px; font-size: 16px; line-height: 23px; color: var(--text-grey);
  }
  .booking { padding: 10px 0 0 25px; }
  .booking__title {
    font-size: 15px; font-weight: 400; color: var(--accent-blue); letter-spacing: 0.3px;
  }
  .booking__steps { list-style: none; margin-top: 6px; }
  .booking__step {
    display: flex; align-items: center; gap: 6px;
    font-size: 13.5px; line-height: 18px; color: var(--text-light);
  }
  .booking__arrow { width: 20px; height: 8px; flex: none; }
  .social-square {
    position: absolute; right: 25px; top: 82px;
    width: 24px; height: 26px; border-radius: 3px;
    background: var(--accent-blue);
  }
</style>
</head>
<body>
  <section class="card card--front">
    <div class="card__hero">
      <div class="hero-photo" role="img" aria-label="Player in a VR headset and vest holding a blaster, arms spread wide"></div>
      <div class="brand">
        <span class="brand__dot"></span>
        <span class="brand__name">Vornik-Play</span>
      </div>
    </div>
    <div class="card__band">
      <div class="contact">
        <p class="contact__phone">813.555.0142</p>
        <p class="contact__address">2716 N Calloway Ave,<br>Tampa, FL 33607, USA</p>
      </div>
    </div>
  </section>

  <section class="card card--back">
    <div class="card__hero">
      <div class="hero-photo" role="img" aria-label="Faint see-through view of the VR player from the front side"></div>
      <div class="brand">
        <span class="brand__name">Vornik-Play</span>
        <span class="brand__dot"></span>
      </div>
    </div>
    <div class="card__band">
      <div class="booking">
        <h2 class="booking__title">BOOKING INSTRUCTIONS</h2>
        <ul class="booking__steps">
          <li class="booking__step"><svg class="booking__arrow" viewBox="0 0 20 8"><circle cx="2" cy="4" r="1.2" fill="#3d52c4"/><circle cx="6" cy="4" r="1.2" fill="#3d52c4"/><path d="M10 4h7M14 1l3 3-3 3" stroke="#5a6fe0" stroke-width="1.6" fill="none"/></svg>www.Vornik-Play.com/book-now</li>
          <li class="booking__step"><svg class="booking__arrow" viewBox="0 0 20 8"><circle cx="2" cy="4" r="1.2" fill="#3d52c4"/><circle cx="6" cy="4" r="1.2" fill="#3d52c4"/><path d="M10 4h7M14 1l3 3-3 3" stroke="#5a6fe0" stroke-width="1.6" fill="none"/></svg>Click on General Admission and input information</li>
          <li class="booking__step"><svg class="booking__arrow" viewBox="0 0 20 8"><circle cx="2" cy="4" r="1.2" fill="#3d52c4"/><circle cx="6" cy="4" r="1.2" fill="#3d52c4"/><path d="M10 4h7M14 1l3 3-3 3" stroke="#5a6fe0" stroke-width="1.6" fill="none"/></svg>Use code Gatepass7 to gain access</li>
          <li class="booking__step"><svg class="booking__arrow" viewBox="0 0 20 8"><circle cx="2" cy="4" r="1.2" fill="#3d52c4"/><circle cx="6" cy="4" r="1.2" fill="#3d52c4"/><path d="M10 4h7M14 1l3 3-3 3" stroke="#5a6fe0" stroke-width="1.6" fill="none"/></svg>See you there!</li>
        </ul>
      </div>
      <span class="social-square" aria-hidden="true"></span>
    </div>
  </section>
</body>
</html>
```